Property Developer Business card design

we need a business card design + printing for a new Property developer company based in melbourne.
We are a group of investors investing in a property developer business. We have more projects involved in residential property as opposed to commercial property but we are involved in both market. we also provide consulting services with overseas investors willing to invest in the australian property market.
Updates
I have uploaded the logo. I'm not very convince with the colors of my logo... any suggestion please?.
Thanks guys!
Target Market(s)
property investors or person willing to purchase investment property
Industry/Entity Type
Residential
Contact Information for Business Card
Tallgrove Holdings Australia Pty Ltd
Look and feel
Each slider illustrates characteristics of the customer's brand and the style your logo design should communicate.

```html
<!DOCTYPE html>
<html lang="en">
<head>
<meta charset="utf-8">
<title>Tallgrove Holdings – Business Card</title>
<link rel="stylesheet" href="https://fonts.googleapis.com/css2?family=Saira+Condensed:wght@500;600;700&display=swap">
<style>
  :root {
    --paper: #ffffff;
    --orange: #e9a232;
    --orange-band: #f0b96c;
    --green: #0e7434;
    --green-mid: #0b6a2f;
    --green-dark: #0a5a28;
    --ink-green: #125a2a;
    --ink-dark: #1d1d1b;
    --name-light: #e6e6e6;
  }
  * { margin: 0; padding: 0; box-sizing: border-box; }
  html, body {
    width: 1200px;
    height: 687px;
    overflow: hidden;
    background: var(--paper);
  }
  .card {
    position: relative;
    width: 1200px;
    height: 687px;
    font-family: "Saira Condensed", "Arial Narrow", sans-serif;
  }
  .card-shapes {
    position: absolute;
    inset: 0;
    width: 1200px;
    height: 687px;
  }
  .orange-panel { fill: var(--orange); }
  .green-panel { fill: var(--green); }
  .green-sweep-1 { fill: var(--green-mid); }
  .green-sweep-2 { fill: var(--green-dark); }
  .company-band { fill: var(--orange-band); }

  .company-name {
    position: absolute;
    left: 35px;
    top: 205px;
    width: 661px;
    height: 56px;
    display: flex;
    align-items: center;
    justify-content: center;
    color: var(--ink-green);
    font-weight: 700;
    font-size: 32px;
    letter-spacing: 1.5px;
    white-space: nowrap;
  }
  .contact-list {
    position: absolute;
    left: 99px;
    top: 448px;
    list-style: none;
    color: var(--ink-dark);
    font-weight: 600;
    font-size: 24px;
    line-height: 33.5px;
    letter-spacing: 1px;
  }
  .contact-list .label {
    display: inline-block;
    width: 96px;
  }
  .person {
    position: absolute;
    left: 838px;
    top: 452px;
    text-align: center;
  }
  .person-name {
    color: var(--name-light);
    font-weight: 600;
    font-size: 52px;
    line-height: 56px;
    letter-spacing: 2px;
    -webkit-text-stroke: 1px #3a3a3a;
  }
  .person-role {
    color: var(--ink-dark);
    font-weight: 600;
    font-size: 23px;
    line-height: 24px;
    letter-spacing: 1.5px;
  }
</style>
</head>
<body>
<main class="card">
  <svg class="card-shapes" viewBox="0 0 1068 611" preserveAspectRatio="none" aria-hidden="true">
    <path class="orange-panel" d="M0,10 H585 C628,150 632,420 440,603 H0 Z"/>
    <path class="green-panel" d="M596,8 H1068 V607 H449 C642,420 638,150 596,8 Z"/>
    <path class="green-sweep-1" d="M728,8 H918 C880,260 730,470 470,606 H455 C660,470 770,260 728,8 Z"/>
    <path class="green-sweep-2" d="M800,8 H852 C830,250 700,470 462,606 H452 C680,460 810,250 800,8 Z"/>
    <rect class="company-band" x="31" y="182" width="588" height="50"/>
  </svg>

  <h1 class="company-name">Tallgrove Holdings Australia Pvt Ltd</h1>

  <ul class="contact-list">
    <li><span class="label">Adress</span>:27/5 Melbourne Australia</li>
    <li><span class="label">Phone</span>:9470318825</li>
    <li><span class="label">Email</span>:dhargrave@tallgrove.com</li>
    <li><span class="label">Website</span>:Tallgrove.aus</li>
  </ul>

  <div class="person">
    <p class="person-name">DANIEL HARGRAVE</p>
    <p class="person-role">Property Developer</p>
  </div>
</main>
</body>
</html>
```